Letterhead and Business card for Brevon Logistics
Brevon Logistics
Letterhead and Business card for Brevon Logistics - Transportation
Creative Brief
Professional
Dirk Makhanya
Manager
17 Kolbe Street Meriton Lindvale Westmark 2841
dirk@brevonlogistics.example

```html
<!DOCTYPE html>
<html lang="en">
<head>
<meta charset="utf-8">
<title>Brevon Logistics Stationery</title>
<link rel="stylesheet" href="https://fonts.googleapis.com/css2?family=Montserrat:wght@400;600;700&display=swap">
<style>
:root{
  --bg:#ececec;
  --paper:#ffffff;
  --ink:#1a1a1a;
  --muted:#6b6b6b;
  --soft:#b4b4b4;
  --rule:#9a9a9a;
}
*{margin:0;padding:0;box-sizing:border-box}
html,body{width:1200px;height:881px;overflow:hidden;background:var(--bg)}
body{position:relative;font-family:'Montserrat',sans-serif;color:var(--ink)}
.sheet{position:absolute;background:var(--paper);box-shadow:0 1px 3px rgba(0,0,0,.12);overflow:hidden}
.brand{display:flex;align-items:center;gap:6px;font-weight:700;white-space:nowrap}
.brand .mark{width:12px;height:12px;background:var(--ink)}
.band{position:absolute;left:0;width:100%;height:8px;display:block}

/* business card front */
.card-front{left:105px;top:149px;width:226px;height:127px}
.card-front .brand{position:absolute;left:12px;top:55px;font-size:9px}
.card-front .person{position:absolute;left:122px;top:24px;font-size:6px;line-height:8px}
.card-front .person strong{display:block;font-size:7.5px}
.card-front .person .role{color:var(--muted);margin-bottom:5px}
.card-front .person p{color:var(--muted);font-size:5px;line-height:7px}
.card-front .band{top:110px}

/* business card back */
.card-back{left:355px;top:149px;width:228px;height:127px;background:var(--ink)}
.card-back .brand{position:absolute;left:0;right:0;top:54px;justify-content:center;color:var(--paper);font-size:13px}
.card-back .brand .mark{background:var(--paper);width:16px;height:16px}

/* envelope front */
.env-front{left:105px;top:377px;width:478px;height:194px}
.env-front .brand{position:absolute;left:18px;top:20px;font-size:9px}
.env-front address{position:absolute;left:18px;top:50px;font-style:normal;font-size:5.5px;line-height:7px;color:var(--muted)}
.env-front .band{top:132px;height:9px}

/* envelope back */
.env-back{left:105px;top:595px;width:478px;height:190px}
.env-back .flap{position:absolute;left:0;top:0}
.env-back .brand{position:absolute;left:0;right:0;top:40px;justify-content:center;color:var(--paper);font-size:15px}
.env-back .brand .mark{background:var(--paper);width:18px;height:18px}

/* letterhead */
.letterhead{left:607px;top:79px;width:497px;height:706px}
.letterhead .brand{position:absolute;left:30px;top:38px;font-size:12px}
.letterhead .brand .mark{width:16px;height:16px}
.letterhead .contact{position:absolute;left:348px;top:30px;font-size:6px;line-height:9px;color:var(--muted)}
.letterhead .contact address{font-style:normal;margin-bottom:6px}
.letterhead .contact li{list-style:none;display:flex;align-items:center;gap:5px}
.letterhead .contact svg{width:7px;height:7px;fill:var(--ink)}
.letterhead .body{position:absolute;left:30px;top:238px;width:440px;font-size:7px;line-height:11px;color:var(--muted);text-align:justify}
.letterhead .body p{margin-bottom:7px}
.letterhead .signature{position:absolute;left:30px;top:596px;width:70px;height:14px;background:linear-gradient(90deg,#d8d8d8,#eeeeee)}
.letterhead .signer{position:absolute;left:30px;top:620px;font-size:7px;line-height:9px}
.letterhead .signer strong{display:block;font-size:8px}
.letterhead .signer span{color:var(--muted)}
.letterhead .band{top:677px}
</style>
</head>
<body>

<section class="sheet card-front">
  <div class="brand"><span class="mark"></span>Brevon Logistics</div>
  <div class="person">
    <strong>Dirk Makhanya</strong>
    <div class="role">Manager</div>
    <p>17 Kolbe Street Meriton</p>
    <p>Lindvale Westmark 2841</p>
    <p>+27 11 555 0142</p>
    <p>dirk@brevonlogistics.example</p>
  </div>
  <svg class="band" viewBox="0 0 226 8" preserveAspectRatio="none">
    <polygon points="0,0 150,0 144,8 0,8" fill="#1a1a1a"/>
    <polygon points="152,3 226,3 226,8 148,8" fill="#b4b4b4"/>
  </svg>
</section>

<section class="sheet card-back">
  <div class="brand"><span class="mark"></span>Brevon Logistics</div>
</section>

<section class="sheet env-front">
  <div class="brand"><span class="mark"></span>Brevon Logistics</div>
  <address>17 Kolbe Street Meriton<br>Lindvale Westmark 2841</address>
  <svg class="band" viewBox="0 0 478 9" preserveAspectRatio="none">
    <polygon points="0,0 340,0 333,9 0,9" fill="#1a1a1a"/>
    <polygon points="343,3 478,3 478,9 338,9" fill="#b4b4b4"/>
  </svg>
</section>

<section class="sheet env-back">
  <svg class="flap" width="478" height="100" viewBox="0 0 478 100">
    <path d="M0,0 H478 V50 Q478,62 462,66 L270,96 Q239,101 208,96 L16,66 Q0,62 0,50 Z" fill="#1a1a1a"/>
  </svg>
  <div class="brand"><span class="mark"></span>Brevon Logistics</div>
</section>

<section class="sheet letterhead">
  <div class="brand"><span class="mark"></span>Brevon Logistics</div>
  <div class="contact">
    <address>17 Kolbe Street Meriton<br>Lindvale Westmark 2841</address>
    <ul>
      <li><svg viewBox="0 0 10 10"><path d="M2,0 L4,2 L3,4 Q4,6 6,7 L8,6 L10,8 L8,10 Q2,9 0,2 Z"/></svg>+27 11 555 0142</li>
      <li><svg viewBox="0 0 10 10"><path d="M0,2 H10 V8 H0 Z M0,2 L5,6 L10,2"/></svg>dirk@brevonlogistics.example</li>
      <li><svg viewBox="0 0 10 10"><circle cx="5" cy="5" r="5"/></svg>www.brevonlogistics.example</li>
    </ul>
  </div>
  <div class="body">
    <p>Lorem ipsum dolor sit amet, consectetur adipiscing elit, sed do eiusmod tempor incididunt ut labore et dolore magna aliqua. Ut enim ad minim veniam, quis nostrud exercitation ullamco laboris nisi ut aliquip ex ea commodo consequat. Duis aute irure dolor in reprehenderit in voluptate velit esse cillum dolore eu fugiat nulla pariatur. Excepteur sint occaecat cupidatat non proident, sunt in culpa qui officia deserunt mollit anim id est laborum. Sed ut perspiciatis unde omnis iste natus error sit voluptatem accusantium doloremque laudantium, totam rem aperiam, eaque ipsa quae ab illo inventore veritatis et quasi architecto beatae vitae dicta sunt explicabo. Nemo enim ipsam voluptatem quia voluptas sit aspernatur aut odit aut fugit, sed quia consequuntur magni dolores eos qui ratione voluptatem sequi nesciunt. Neque porro quisquam est, qui dolorem ipsum quia dolor sit amet.</p>
    <p>Lorem ipsum dolor sit amet, consectetur adipiscing elit, sed do eiusmod tempor incididunt ut labore et dolore magna aliqua. Ut enim ad minim veniam, quis nostrud exercitation ullamco laboris nisi ut aliquip ex ea commodo consequat. Duis aute irure dolor in reprehenderit in voluptate velit esse cillum dolore eu fugiat nulla pariatur. Excepteur sint occaecat cupidatat non proident, sunt in culpa qui officia deserunt mollit anim id est laborum. Sed ut perspiciatis unde omnis iste natus error sit voluptatem accusantium doloremque laudantium, totam rem aperiam, eaque ipsa quae ab illo inventore veritatis et quasi architecto beatae vitae dicta sunt explicabo. Nemo enim ipsam voluptatem quia voluptas sit aspernatur aut odit aut fugit, sed quia consequuntur magni dolores eos qui ratione voluptatem sequi nesciunt.</p>
  </div>
  <div class="signature" role="img" aria-label="Handwritten signature of Dirk Makhanya"></div>
  <div class="signer"><strong>Dirk Makhanya</strong><span>Manager</span></div>
  <svg class="band" viewBox="0 0 497 8" preserveAspectRatio="none">
    <polygon points="0,0 300,0 294,8 0,8" fill="#1a1a1a"/>
    <polygon points="302,3 497,3 497,8 298,8" fill="#9a9a9a"/>
  </svg>
</section>

</body>
</html>
```